Modern Lawfirm Business Card Design

We're looking for a business card to incorporate the newly created logo we had made.

Ideally looking for a law firm business card demonstrating, modern, minimalist, strong/bold design.

I'm open to any design honestly, but nothing "flashy".

Target Market(s)

Immigration law, family immigration, humanitarian, general legal

Industry/Entity Type

Law Firm

Contact Information for Business Card

Please use dummy information, name, street address, city, state, phone number, email, website.

Font styles to use
Serif
Sans Serif

Requirements
Must have
• Please use dummy information, name, street address, city, state, phone number, email, website.

```html
<!DOCTYPE html>
<html lang="en">
<head>
<meta charset="utf-8">
<title>Valcourt Immigration Law — Business Card</title>
<link href="https://fonts.googleapis.com/css2?family=Libre+Baskerville:wght@700&family=Open+Sans:wght@400;600&display=swap" rel="stylesheet">
<style>
  :root {
    --backdrop: #e9e9e9;
    --card-white: #fbfbfb;
    --brand-blue: #1c4882;
    --text-grey: #3a3a3a;
    --white: #ffffff;
  }
  * { margin: 0; padding: 0; box-sizing: border-box; }
  html, body { width: 1200px; height: 900px; overflow: hidden; }
  body {
    background: var(--backdrop);
    position: relative;
    font-family: "Open Sans", Arial, sans-serif;
  }
  .card {
    position: absolute;
    top: 307px;
    width: 500px;
    height: 286px;
    box-shadow: 0 10px 30px rgba(0,0,0,0.12);
  }
  .card--front { left: 70px; background: var(--card-white); }
  .card--back { left: 630px; background: var(--brand-blue); }

  .holder { position: absolute; left: 34px; top: 30px; }
  .holder__name {
    font-family: "Libre Baskerville", Georgia, serif;
    font-weight: 700;
    font-size: 15px;
    letter-spacing: 0.5px;
    color: var(--brand-blue);
  }
  .holder__title { font-size: 11px; color: var(--text-grey); margin-top: 2px; }

  .contacts { position: absolute; left: 34px; top: 118px; list-style: none; }
  .contacts li {
    display: flex; align-items: center; gap: 7px;
    font-size: 11.5px; color: var(--text-grey); line-height: 19px;
  }
  .contacts svg { width: 10px; height: 10px; fill: var(--brand-blue); flex: none; }

  .firm-name {
    display: flex; align-items: center; gap: 8px;
    font-family: "Open Sans", Arial, sans-serif;
    font-weight: 600;
    white-space: nowrap;
  }
  .firm-name__square { width: 12px; height: 12px; flex: none; }

  .card--front .firm-name {
    position: absolute; right: 30px; top: 122px;
    font-size: 17px; color: var(--brand-blue);
  }
  .card--front .firm-name__square { background: var(--brand-blue); }

  .card--back .firm-name {
    position: absolute; left: 0; right: 0; top: 102px;
    justify-content: center;
    font-size: 24px; color: var(--white);
  }
  .card--back .firm-name__square { width: 16px; height: 16px; background: var(--white); }

  .back-site {
    position: absolute; left: 0; right: 0; top: 196px;
    text-align: center; font-size: 12px; color: var(--white);
  }
</style>
</head>
<body>
  <section class="card card--front">
    <div class="holder">
      <p class="holder__name">DANIEL HARTLEY</p>
      <p class="holder__title">Managing Director</p>
    </div>
    <ul class="contacts">
      <li><svg viewBox="0 0 10 10"><path d="M2 0.5 L3.8 2.6 L2.9 3.6 Q4 6 6.4 7.1 L7.4 6.2 L9.5 8 L8.3 9.5 Q1.5 8 0.5 1.7 Z"/></svg>(044)123456789</li>
      <li><svg viewBox="0 0 10 10"><path d="M0.5 2 H9.5 V8 H0.5 Z M1 2.4 L5 5.4 L9 2.4" fill="none" stroke="#1c4882" stroke-width="1"/></svg>info@youremail.com</li>
      <li><svg viewBox="0 0 10 10"><circle cx="5" cy="5" r="4.5"/></svg>www.websitename.com</li>
      <li><svg viewBox="0 0 10 10"><path d="M5 0.3 A3.4 3.4 0 0 1 8.4 3.7 C8.4 6 5 9.7 5 9.7 C5 9.7 1.6 6 1.6 3.7 A3.4 3.4 0 0 1 5 0.3 Z"/></svg>1234, Address GoesHere, Country name, 12345</li>
    </ul>
    <p class="firm-name"><span class="firm-name__square"></span>Valcourt Immigration Law</p>
  </section>

  <section class="card card--back">
    <p class="firm-name"><span class="firm-name__square"></span>Valcourt Immigration Law</p>
    <p class="back-site">www.websitename.com</p>
  </section>
</body>
</html>
```